Fruit and veg boxes + online deli

I need a flyer that showcases my four different types of fruit and veg boxes: small £8.50, medium &14, large £19.50, build your own box -(minimum spend is £5/each item is individually priced).
It must also illustrate my online deli feature. We sell cheeses, meat, fish, gourmet pies, tray bakes and bread baked in house.
Folded A4 horizontal leaflet, so four sided.
We're a small UK start up online green grocer.
We promote our service by offering a free trial box (small box only). The design must focus heavily on this.
We promote local and regional agriculture.

Target Market(s)

All residential households

Industry/Entity Type

Build

Font styles to use
Decorative

Requirements
Must have
• Here is my website so you can get the general feel of my service
• www.brookvalecrate.co.uk
• Cover page must emphasize heavily on our free trial offer.
• Our 4 different types of boxes on page 2
• Our deli on page 3/4
• Our contact details / website visible on pages 2/3/4
Nice to have
• Nice to tell the reader that we're a small UK start up online greengrocer.
• We offer a different alternative to supermarket shopping by offering hand made delicatessen..

```html
<!DOCTYPE html>
<html lang="en">
<head>
<meta charset="utf-8">
<title>Brookvale Crate – folded leaflet</title>
<link rel="stylesheet" href="https://fonts.googleapis.com/css2?family=Oswald:wght@300;400&family=Alegreya:wght@400;700&family=Open+Sans:wght@400&display=swap">
<style>
:root{
  --sheet:#d3d3d3;
  --cream:#f8ecd2;
  --chalk:#1e1e1e;
  --white:#ffffff;
  --gold:#e0a31c;
  --ink:#3a3226;
  --wood:#c98f4e;
  --wood-dark:#8a5426;
  --label:#222222;
}
*{box-sizing:border-box;margin:0;padding:0}
html,body{width:862px;height:1200px;overflow:hidden}
body{background:var(--sheet);position:relative;font-family:"Alegreya",serif}
.view-label{position:absolute;font-family:"Open Sans",sans-serif;font-size:26px;color:var(--label);transform:translateX(-50%)}
.spread{position:absolute;overflow:hidden}
.spread--outer{left:78px;top:90px;width:712px;height:504px}
.spread--inner{left:78px;top:660px;width:708px;height:500px;background:var(--cream)}
.photo{position:absolute}
.chalk-panel{position:absolute;background:var(--chalk);color:var(--white);text-align:center}
.chalk-panel .stars{font-size:10px;letter-spacing:1px;margin:6px 0}
.custom-box{left:88px;top:54px;width:184px;height:302px;padding:52px 14px 0}
.custom-box h2{font-size:20px;line-height:22px;font-weight:400}
.custom-box ul{list-style:none;text-align:left;font-size:12.5px;line-height:14px;margin-top:6px}
.custom-box li{padding-left:10px;position:relative;margin-bottom:8px}
.custom-box li::before{content:"";position:absolute;left:0;top:5px;width:4px;height:4px;background:var(--gold);transform:rotate(45deg)}
.custom-box p{font-size:9px;line-height:11.5px;margin-top:4px}
.band{position:absolute;left:0;width:100%;background:var(--cream)}
.band--outer{top:390px;height:58px}
.band__order{position:absolute;left:78px;top:8px;width:200px;text-align:center;font-family:"Oswald",sans-serif;color:var(--ink)}
.band__order .lead{font-size:11px;font-weight:300}
.band__order .url{font-size:13.5px;color:var(--gold)}
.band__order .mail{font-family:"Open Sans",sans-serif;font-size:5.5px;color:var(--ink)}
.brand{position:absolute;left:380px;top:8px;display:flex;align-items:center;gap:8px}
.brand__mark{width:20px;height:20px;background:var(--gold)}
.brand__name{font-family:"Oswald",sans-serif;font-size:28px;color:var(--ink);line-height:30px}
.brand__tag{position:absolute;left:456px;top:44px;font-family:"Open Sans",sans-serif;font-size:6px;color:var(--ink);letter-spacing:.3px}
.sign{position:absolute;background:linear-gradient(180deg,#d9a466,var(--wood));color:#3a2410;font-family:"Oswald",sans-serif;text-align:center;border-radius:2px;box-shadow:0 2px 4px rgba(0,0,0,.35)}
.sign--trial{left:400px;top:94px;width:210px;height:106px;transform:rotate(-8deg);padding-top:10px}
.sign--trial .big{font-size:32px;line-height:36px}
.sign--trial .mid{font-size:19px;line-height:22px}
.sign--trial .url{font-size:13px;line-height:18px}
.sign--about{left:538px;top:220px;width:140px;height:80px;transform:rotate(16deg);font-size:9.5px;line-height:11px;padding:12px 10px;font-weight:300}
.prepacked{left:30px;top:34px;width:182px;height:374px;padding-top:40px;font-family:"Oswald",sans-serif}
.prepacked h2{font-size:22px;font-weight:300}
.box-tier{margin-top:4px}
.box-tier h3{font-size:13px;font-weight:300}
.box-tier .row{display:flex;justify-content:center;gap:10px;text-align:left}
.box-tier .meta{font-size:6.5px;font-weight:300;line-height:11px;width:52px;padding-top:4px}
.box-tier .price{font-size:17px;font-weight:300;line-height:19px}
.box-tier .opts{font-size:6.5px;font-weight:300;line-height:8.5px}
.col{position:absolute;color:var(--ink)}
.col h2{font-family:"Oswald",sans-serif;font-weight:300;font-size:14px;color:var(--gold)}
.col .sub{font-family:"Oswald",sans-serif;font-weight:300;font-size:9.5px;line-height:13px;margin-top:2px}
.col .sub em{font-style:normal;color:var(--gold)}
.col p{font-size:5.6px;line-height:8.5px;margin-top:6px}
.col--boxes{left:223px;top:36px;width:106px}
.col--deli{left:379px;top:36px;width:100px}
.deli-list{list-style:none;font-size:5.6px;line-height:10.5px;margin-top:12px}
.deli-list li::before{content:"✤ ";color:var(--gold)}
.sign--pies{left:598px;top:196px;width:84px;height:42px;transform:rotate(8deg);padding-top:5px}
.sign--deli{left:570px;top:316px;width:118px;height:46px;transform:rotate(-8deg);padding-top:5px}
.sign .h{font-size:13px;line-height:15px}
.sign .s{font-size:8px;font-weight:300}
.band--inner{top:574px;height:32px}
.band--inner{top:442px}
.band__line{position:absolute;left:0;right:0;top:4px;text-align:center;font-family:"Oswald",sans-serif;font-size:15px;font-weight:300;color:var(--ink)}
.band__mail{position:absolute;left:0;right:0;top:24px;text-align:center;font-family:"Open Sans",sans-serif;font-size:5px;color:var(--ink)}
.gold-lines{position:absolute;left:0;top:0}
</style>
</head>
<body>

<div class="view-label" style="left:256px;top:42px">Back</div>
<div class="view-label" style="left:610px;top:42px">Front</div>

<section class="spread spread--outer">
  <div class="photo" role="img" aria-label="Wooden crate of fresh vegetables on a rustic wood table" style="inset:0;background:linear-gradient(120deg,#b7793f 0%,#8f5a2c 35%,#5d6b2a 55%,#b33a24 70%,#6a3d2a 100%)"></div>

  <div class="chalk-panel custom-box">
    <h2>Build Your Own<br>Custom Box</h2>
    <div class="stars">****</div>
    <ul>
      <li>Stay in control over what goes in your box.</li>
      <li>Manage exactly how much you want to spend on fresh fruit and veg.</li>
    </ul>
    <p>We now have an exciting new “build your own box” shopping facility which allows you to move away from the pre-picked small/medium/large box and to shop for items individually.</p>
  </div>

  <div class="sign sign--trial">
    <div class="big">FREE TRIAL BOX</div>
    <div class="mid">Order your box today</div>
    <div class="url">www.brookvalecrate.co.uk</div>
  </div>
  <div class="sign sign--about">We're a small UK start up online greengrocer. We offer a different alternative for those tired and fed up of their local supermarket.</div>

  <div class="band band--outer">
    <div class="band__order">
      <div class="lead">Order your box today:</div>
      <div class="url">www.brookvalecrate.co.uk</div>
      <div class="mail">✉ info@brookvalecrate.co.uk</div>
    </div>
    <div class="brand">
      <span class="brand__mark"></span>
      <span class="brand__name">Brookvale Crate</span>
    </div>
    <div class="brand__tag">Bringing you the very best fruit &amp; veg direct to your doorstep</div>
  </div>
</section>

<div class="view-label" style="left:256px;top:622px">Inside left</div>
<div class="view-label" style="left:610px;top:622px">Inside right</div>

<section class="spread spread--inner">
  <div class="photo" role="img" aria-label="Blueberries on dark wood" style="left:0;top:40px;width:60px;height:400px;background:linear-gradient(180deg,#2f3f63,#1d2640)"></div>
  <div class="photo" role="img" aria-label="Bowl of strawberries and blueberries" style="left:0;top:400px;width:300px;height:100px;background:linear-gradient(90deg,#b3202a,#7c1a22 60%,#3a4660)"></div>
  <div class="photo" role="img" aria-label="Sliced red onion and peppercorns" style="left:223px;top:170px;width:106px;height:118px;background:linear-gradient(135deg,#6d7f3a,#8a2a4a 45%,#e8d8de 70%,#5a3a32)"></div>
  <div class="photo" role="img" aria-label="Fresh raspberries" style="left:212px;top:288px;width:118px;height:154px;background:linear-gradient(160deg,#d3304a,#a01830);clip-path:polygon(0 0,55% 0,100% 55%,100% 100%,0 100%)"></div>
  <div class="photo" role="img" aria-label="Jug of fresh juice with fruit" style="left:379px;top:290px;width:84px;height:152px;background:linear-gradient(180deg,#e8b97a,#f2ecd8 50%,#b8c27a)"></div>
  <div class="photo" role="img" aria-label="Golden baked gourmet pie" style="left:464px;top:0;width:244px;height:230px;background:linear-gradient(150deg,#6b5a4a,#c88a3e 45%,#e3b46a 70%,#7a6a5a);clip-path:polygon(22% 0,100% 0,100% 100%,40% 100%,0 40%)"></div>
  <div class="photo" role="img" aria-label="Loaf of seeded bread sliced" style="left:498px;top:150px;width:84px;height:100px;background:linear-gradient(135deg,#6a4a30,#a87a50 60%,#d8c8b0)"></div>
  <div class="photo" role="img" aria-label="Fish cakes on a plate" style="left:498px;top:260px;width:84px;height:86px;background:linear-gradient(135deg,#e9e4da,#c98a3a 50%,#a7b062)"></div>
  <div class="photo" role="img" aria-label="Sliced cooked ham" style="left:498px;top:356px;width:84px;height:86px;background:linear-gradient(135deg,#f0ebe4,#e6a7a0 55%,#c98b84)"></div>
  <div class="photo" role="img" aria-label="Fresh spinach leaves" style="left:590px;top:400px;width:118px;height:100px;background:linear-gradient(135deg,#4e8a2a,#2e5a18);clip-path:polygon(100% 0,100% 100%,0 100%)"></div>

  <svg class="gold-lines" width="708" height="500" viewBox="0 0 708 500" aria-hidden="true">
    <g fill="none" stroke="#e0a31c" stroke-width="1">
      <polyline points="0,95 30,118"/>
      <polyline points="360,0 485,0"/>
      <polyline points="468,0 460,20"/>
      <polyline points="568,0 492,80 492,150"/>
      <polyline points="690,230 640,282"/>
      <polyline points="660,60 708,10"/>
    </g>
  </svg>

  <div class="chalk-panel prepacked">
    <h2>Pre-packed boxes</h2>
    <div class="stars">****</div>
    <div class="box-tier">
      <h3>Large Box</h3>
      <div class="row"><div class="meta">Suitable for 4–6 people<br>Available as</div><div><div class="price">£19.50</div><div class="opts">✤ fruit only<br>✤ Veg only<br>✤ Mixed Fruit &amp; Veg</div></div></div>
    </div>
    <div class="stars">****</div>
    <div class="box-tier">
      <h3>Medium Box</h3>
      <div class="row"><div class="meta">Suitable for 2–4 people<br>Available as</div><div><div class="price">£14.00</div><div class="opts">✤ fruit only<br>✤ Veg only<br>✤ Mixed Fruit &amp; Veg</div></div></div>
    </div>
    <div class="stars">****</div>
    <div class="box-tier">
      <h3>Small Essencial Box</h3>
      <div class="row"><div class="meta">Suitable for 1–2 people<br>Available as</div><div><div class="price">£8.50</div><div class="opts">✤ fruit only<br>✤ Veg only<br>✤ Mixed Fruit &amp; Veg</div></div></div>
    </div>
  </div>

  <div class="col col--boxes">
    <h2>Pre-packed boxes</h2>
    <div class="sub">Receive your first delivery from us for <em>FREE.</em></div>
    <p style="margin-top:1px">(£2.00 delivery charge and further terms apply).</p>
    <p>Our fruit and vegetable boxes are full of farm fresh goodness, delivered overnight directly to your doorstep. We offer 3 different size boxes to suit your household needs, or you can make up your own box with exactly what you want using our new “Build Your Own Box” feature.</p>
  </div>

  <div class="col col--deli">
    <h2>line Deli</h2>
    <div class="sub">“Full of <em>AWARD<br>WINNING</em> food”</div>
    <p>You can also choose to have any of the following products to be delivered alongside your fruit and veg box.</p>
    <ul class="deli-list">
      <li>Bread, Eggs &amp; Dairy</li>
      <li>Fruit Juices &amp; Soups</li>
      <li>My Meat Box</li>
      <li>Gourmet Sausages &amp; Pate</li>
      <li>Pies &amp; Ready Made Meals</li>
      <li>Weekend Treats &amp; Snacks</li>
      <li>Desserts</li>
      <li>Jams, Curds &amp; Honey</li>
      <li>Fish</li>
      <li>Vegetarian &amp; Gluten Free Deli</li>
      <li>Risotto &amp; Couscous</li>
      <li>Tea, Coffee, Biscuits &amp; Cereals</li>
      <li>Cooking Sauces &amp; Condiments</li>
      <li>Herbs &amp; More Fresh Produce</li>
      <li>For The Store Cupboard</li>
    </ul>
  </div>

  <div class="sign sign--pies"><div class="h">LUXURY PIES</div><div class="s">made to order</div></div>
  <div class="sign sign--deli"><div class="h">OUR ONLINE DELI</div><div class="s">full of award winning food</div></div>

  <div class="band band--inner">
    <div class="band__line">Order your box today: www.brookvalecrate.co.uk</div>
    <div class="band__mail">✉ info@brookvalecrate.co.uk</div>
  </div>
</section>

</body>
</html>
```